Digital Menu Board for Restaurant

I want a digital menu board for our new restaurant. I have provided the sample of what I kind of want.
This is to be on a 55 inch tv so it needs to be the correct aspect ratio of 4:5

Font styles to use
Serif
Sans Serif

Colors
f59296
f04a50
ec1f27
ffffff
fffef7
fbed22
ffc214
0592cd
e5519f

Requirements
Must have
• fun, maybe something moving? bright colors on a darker background so it's easy to read or dark font on a light background.

```html
<!DOCTYPE html>
<html lang="en">
<head>
<meta charset="utf-8">
<title>Sandy Shores Menu Board</title>
<link rel="stylesheet" href="https://fonts.googleapis.com/css2?family=Questrial&family=Roboto+Condensed:wght@700&family=Mulish:wght@700;800&display=swap">
<style>
  :root {
    --board: #2b2d33;
    --yellow: #fbed22;
    --gold: #ffc214;
    --red: #ec1f27;
    --coral: #f04a50;
    --blue: #0592cd;
    --white: #ffffff;
    --cream: #fffef7;
    --olive: #8a7f2a;
  }
  * { margin: 0; padding: 0; box-sizing: border-box; }
  html, body { width: 1200px; height: 1200px; overflow: hidden; background: var(--white); }
  .stage { position: relative; width: 1500px; height: 1500px; transform: scale(0.8); transform-origin: 0 0; }
  .board { position: absolute; left: 341px; top: 22px; width: 819px; height: 1456px; background: var(--board); }
  .frame { position: absolute; left: 8px; top: 8px; width: 803px; height: 1316px; border: 3px solid var(--yellow); }
  .abs { position: absolute; }
  .brand { left: 60px; top: 95px; width: 380px; display: flex; align-items: center; gap: 14px;
    font-family: "Questrial", sans-serif; font-size: 50px; color: var(--coral); }
  .brand-dot { width: 34px; height: 34px; border-radius: 50%; background: var(--gold); flex: none; }
  .combo { left: 440px; top: 25px; width: 370px; height: 156px; background: var(--yellow);
    clip-path: polygon(0 0, 100% 0, 100% 100%, 0 100%, 8px 50%);
    font-family: "Mulish", sans-serif; font-weight: 800; color: #1e1f22; text-align: center; padding-top: 10px; }
  .combo h2 { font-size: 32px; font-weight: 800; line-height: 40px; }
  .combo p { font-size: 25px; line-height: 31px; }
  .tag { font-family: "Roboto Condensed", sans-serif; font-weight: 700; line-height: 1; display: flex; align-items: center; }
  .tag-buns { left: 9px; top: 261px; width: 276px; height: 57px; background: var(--yellow); color: #1e1f22; font-size: 36px; padding-left: 9px;
    clip-path: polygon(0 0, 100% 0, 94% 100%, 0 100%); }
  .buns-box { left: 9px; top: 289px; width: 391px; height: 560px; border: 1.5px solid var(--olive); border-left: none; }
  .tag-green { left: 425px; top: 261px; width: 276px; height: 57px; background: var(--blue); color: var(--white); font-size: 36px; padding-left: 9px;
    clip-path: polygon(0 0, 100% 0, 96% 100%, 0 100%); }
  .band { background: var(--red); color: var(--white); font-size: 30px; padding-left: 12px; }
  .band-sides { left: 9px; top: 875px; width: 390px; height: 45px; }
  .band-kids { left: 422px; top: 701px; width: 388px; height: 45px; }
  .band-drinks { left: 422px; top: 911px; width: 388px; height: 45px; }
  .item h3 { font-family: "Questrial", sans-serif; font-weight: 400; font-size: 30px; color: var(--white); line-height: 32px; -webkit-text-stroke: 0.4px var(--white); }
  .item p { font-family: "Mulish", sans-serif; font-weight: 700; font-size: 16.5px; line-height: 20.3px; color: var(--yellow); margin-top: 4px; }
  .col-left { left: 18px; }
  .col-right { left: 434px; }
  .list { font-family: "Questrial", sans-serif; font-size: 24px; line-height: 28.6px; color: var(--cream); -webkit-text-stroke: 0.3px var(--cream); }
  .list .dash { color: var(--red); }
  .shakes-rule { left: 9px; top: 1114px; width: 801px; height: 3px; background: var(--yellow); }
  .shakes-label { left: 340px; top: 1097px; width: 120px; background: var(--board); color: var(--yellow);
    font-family: "Roboto Condensed", sans-serif; font-weight: 700; font-size: 30px; text-align: center; line-height: 36px; }
  .shakes { left: 0; top: 1136px; width: 819px; text-align: center; }
  .footer { left: 0; top: 1326px; width: 819px; height: 130px; background: var(--yellow);
    font-family: "Mulish", sans-serif; font-weight: 800; font-size: 46px; color: #2b2d33; display: flex; align-items: center; justify-content: center; }
</style>
</head>
<body>
<div class="stage">
  <div class="board">
    <div class="frame"></div>

    <div class="abs brand"><span class="brand-dot"></span>Sandy Shores</div>

    <div class="abs combo">
      <h2>COMBO UP!</h2>
      <p>ADD 1 SIDE AND DRINK</p>
      <p>ADD 1 SIDE AND SHAKE</p>
      <p>ADDITIONAL SIDES</p>
    </div>

    <div class="abs buns-box"></div>
    <div class="abs tag tag-buns">BETWEEN BUNS</div>
    <div class="abs tag tag-green">GREEN SHORE</div>

    <div class="abs item col-left" style="top:328px">
      <h3>1st Point Pulled Pork</h3>
      <p>Pulled Pork, Marty’s Sassy BBQ Sauce,<br>Chopped Bacon, Pepperjack Cheese, and<br>Fried Jalapeno Peppers on a Ciabatta Bun</p>
    </div>
    <div class="abs item col-left" style="top:436px">
      <h3>2nd Point Pulled Pork</h3>
      <p>Pulled Pork, Marty’s Sweet Raspberry<br>BBQ Sauce,and coleslaw on a Ciabatta Bun</p>
    </div>
    <div class="abs item col-left" style="top:524px">
      <h3>Spiniker Point Burger</h3>
      <p>Smokehouse ½ Pound Burger, Crumbled<br>Bacon, Marty’s Sassy BBQ Sauce, Cheese,<br>and Onion Ring on a Toasted Brioche Bun</p>
    </div>
    <div class="abs item col-left" style="top:633px">
      <h3>The Rock Burger</h3>
      <p>Two Smokehouse ½ Pound Patties, Cheese,<br>Lettuce, Tomato, Onion, Pickles,<br>on Toasted Brioche Bun</p>
    </div>
    <div class="abs item col-left" style="top:740px">
      <h3>Rainbow Cove Sandwich</h3>
      <p>Chicken Salad - Smoke Chicken, Celery, and<br>Onion Mixed with our BBQ Mayo and Topped<br>with Seasoned Tomato on a Hoagie Roll</p>
    </div>

    <div class="abs item col-right" style="top:328px">
      <h3>North Beach Salad</h3>
      <p>Pulled Pork and Black Beans on a Bed of<br>Romaine, Tomato and Onion with Sweet and<br>Sour Raspberry Pineapple Sauce</p>
    </div>
    <div class="abs item col-right" style="top:436px">
      <h3>West Side Salad</h3>
      <p>BBQ Pulled Pork, Crumbled Bacon, Candied<br>Walnuts, Feta Cheese, Red Onion, Spinach<br>and Lettuce with Ranch Dressing or Raspberry<br>Vinaigrette</p>
    </div>
    <div class="abs item col-right" style="top:562px">
      <h3>East Side Salad</h3>
      <p>Spinach and Lettuce, Chopped Apples,<br>Candied Walnuts, Onion, Feta Cheese with<br>Marty’s Raspberry Vinaigrette<br>Add Chicken:</p>
    </div>

    <div class="abs tag band band-kids">SEASHELL FINDERS (KIDS)</div>
    <div class="abs list col-right" style="top:752px">
      Little Cheeseburger<br>Pulled Pork Sandwich<br>Mini Corn Dogs<br>Chicken Salad Sandwich<br>Fries / Onion Rings
    </div>

    <div class="abs tag band band-drinks">DRINKS</div>
    <div class="abs list col-right" style="top:962px">
      Fizz Cola <span class="dash">-</span> Diet Fizz<br>
      Bolt Cola <span class="dash">-</span> Diet Bolt<br>
      Peak Soda <span class="dash">-</span> Diet Peak<br>
      Lemonade <span class="dash">-</span> Lemon Lime <span class="dash">-</span> Pepper Fizz
    </div>

    <div class="abs tag band band-sides">SIDES</div>
    <div class="abs list" style="left:21px; top:930px">
      Seasoned Fries<br>Onion Rings<br>Sweet Cornbread<br>Sweet Coleslaw<br>Macaroni Salad<br>Side Salad
    </div>

    <div class="abs shakes-rule"></div>
    <div class="abs shakes-label">SHAKES</div>
    <div class="abs list shakes">
      Marty’s Signature Raspberry Jammin Shake<br>
      Raspberry Cookie Crumble Shake<br>
      Raspberry Hazelnut Bomb Shake<br>
      Raspberry Beachin’ Shake (Pine Colada)<br>
      Raspberry Brownie Sake<br>
      Caramel Shake
    </div>

    <div class="abs footer">Enjoy Our Meal</div>
  </div>
</div>
</body>
</html>
```